Easter & Summer School Dance Camps

I need two flyers one for Easter camps and one for summer school
We are a performing arts and dance academy

I want a double sided flyers one side summer school one side easter camp

Please make these flyers appeal to young dancers and performers - eye catching up to date Added Tuesday, March 1, 2016

Target Market(s)

Young children and teenagers

Industry/Entity Type

School

Font styles to use
Serif
Sans Serif

Requirements
Must have
• bright colourful

```html
<!DOCTYPE html>
<html lang="en">
<head>
<meta charset="utf-8">
<title>Brightstep Easter Dance Camp Flyer</title>
<link href="https://fonts.googleapis.com/css2?family=Bubblegum+Sans&display=swap" rel="stylesheet">
<style>
  :root {
    --page: #ececec;
    --green: #9fcf7f;
    --green-stripe: #b3da98;
    --green-dark: #5faa3e;
    --pink: #e8368f;
    --orange: #f29111;
    --white: #ffffff;
    --ink: #222222;
  }
  html, body {
    margin: 0;
    padding: 0;
    overflow: hidden;
  }
  body {
    width: 797px;
    height: 1200px;
    background: var(--page);
    position: relative;
    font-family: "Bubblegum Sans", sans-serif;
  }
  .flyer {
    position: absolute;
    left: 38px;
    top: 345px;
    width: 720px;
    height: 510px;
    background: repeating-linear-gradient(115deg, var(--green) 0 22px, var(--green-stripe) 22px 34px);
    box-shadow: 0 6px 18px rgba(0,0,0,0.18);
    overflow: hidden;
  }
  .badge {
    position: absolute;
    background: var(--white);
    border-radius: 50%;
    display: flex;
    align-items: center;
    justify-content: center;
    text-align: center;
    box-sizing: border-box;
  }
  .badge::after {
    content: "";
    position: absolute;
    inset: 7px;
    border-radius: inherit;
    border: 3px dashed var(--accent);
  }
  .badge p, .badge h1 {
    margin: 0;
    font-weight: 400;
    position: relative;
    z-index: 1;
  }
  .badge--logo { --accent: var(--pink); left: 30px; top: 80px; width: 210px; height: 170px; }
  .badge--title { --accent: var(--green-dark); left: 258px; top: 40px; width: 225px; height: 160px; }
  .badge--price { --accent: var(--orange); left: 505px; top: 15px; width: 195px; height: 150px; }
  .badge--dates { --accent: var(--orange); left: 58px; top: 325px; width: 200px; height: 165px; }
  .badge--venue { --accent: var(--pink); left: 545px; top: 265px; width: 160px; height: 135px; }
  .badge--contact { --accent: var(--green-dark); left: 255px; top: 390px; width: 300px; height: 88px; border-radius: 44px; }

  .brand {
    display: flex;
    align-items: center;
    gap: 8px;
    font-size: 38px;
    color: var(--ink);
    position: relative;
    z-index: 1;
  }
  .brand-dot {
    width: 14px;
    height: 14px;
    border-radius: 50%;
    background: var(--pink);
  }
  .title {
    font-size: 33px;
    line-height: 1.1;
    color: var(--green-dark);
    letter-spacing: 1px;
  }
  .price {
    font-size: 25px;
    line-height: 1.2;
    color: var(--orange);
  }
  .dates {
    font-size: 20px;
    line-height: 1.2;
    color: var(--orange);
  }
  .venue {
    font-size: 16px;
    line-height: 1.15;
    color: var(--pink);
  }
  .contact {
    font-size: 17px;
    line-height: 1.25;
    color: var(--green-dark);
  }
  .pitch {
    position: absolute;
    left: 268px;
    top: 218px;
    width: 268px;
    margin: 0;
    font-size: 28px;
    line-height: 1.2;
    color: var(--white);
    text-align: center;
  }
  .pitch .fun { color: var(--pink); }
  .pitch .fresh { color: var(--green-dark); }
  .pitch .funky { color: var(--orange); }
</style>
</head>
<body>
  <section class="flyer" aria-label="Easter dance camp flyer">
    <div class="badge badge--logo">
      <div class="brand"><span class="brand-dot"></span>Brightstep</div>
    </div>
    <div class="badge badge--title">
      <h1 class="title">WEST END<br>WORKSHOP</h1>
    </div>
    <div class="badge badge--price">
      <p class="price">£30 per day/<br>£55 for both</p>
    </div>
    <p class="pitch">Our Easter dance camps are <span class="fun">fun</span>, <span class="fresh">fresh</span> and <span class="funky">funky</span>, mixed together with a little musical theatre!</p>
    <div class="badge badge--dates">
      <p class="dates">Tue &amp; Wed 5 &amp; 6<br>April 2016<br>5–16 years<br>10am–4pm</p>
    </div>
    <div class="badge badge--venue">
      <p class="venue">Venue<br>The Village Hall<br>of St Aldric<br>Elmbrook<br>KT9 1ZZ</p>
    </div>
    <div class="badge badge--contact">
      <p class="contact">Email brightstepdance@mailbox<br>to book or text 07700900482</p>
    </div>
  </section>
</body>
</html>
```